Mental Health Therapy Website

I need a design for a mental health therapy website. It is a private practice. The business name is Brindle Counseling, PLLC. My name is Martin Hale, LMHC, NCC, DCC. I would like some of the features/menus to be Home; Welcome/About Me, Rates and Services, Common Questions, and Contact.
If possible I would like a blog on the main page that I can update with articles I write. I would like the contact page to feature a map to my location (4318 Cedarbend Ave. E, Lakewood, WA 98499).
I would like to place a small photo of me on the Welcome/About page.
I am new to this so if I am forgetting anything, please ask me!!
I will upload my logo so you can fit it and the color scheme into the design.
Thank you so very much!

```html
<!DOCTYPE html>
<html lang="en">
<head>
<meta charset="utf-8">
<title>Brindle Counseling, PLLC</title>
<link rel="stylesheet" href="https://fonts.googleapis.com/css2?family=Cinzel:wght@400;700&family=Arimo:wght@400;700&display=swap">
<style>
:root{
  --black:#000;
  --green:#6c9a2c;
  --green-light:#8cc63f;
  --green-dark:#4f7a1c;
  --blue:#2a5a97;
  --blue-line:#a9c2e3;
  --logo-blue:#1f4f8f;
  --white:#fff;
  --text:#3a3a3a;
  --footer:#2b2b2b;
  --map:#ece5d6;
}
*{margin:0;padding:0;box-sizing:border-box}
html,body{width:1200px;height:2696px;overflow:hidden;background:var(--white)}
body{position:relative;font-family:"Arimo",Arial,sans-serif;color:var(--text)}
a{text-decoration:none}
h1,h2,h3{font-weight:400}

/* Hero */
.hero{position:absolute;left:0;top:0;width:1200px;height:734px;background:var(--black);overflow:hidden}
.hero-visual{position:absolute;left:0;top:0;width:1200px;height:734px;
  background:radial-gradient(ellipse 420px 380px at 560px 380px,#3186c6 0%,#1a5189 40%,#0a1f38 75%,#000 100%)}
.logo-tab{position:absolute;left:440px;top:0;width:320px;height:126px;background:var(--white);border-radius:0 0 60px 60px;
  display:flex;align-items:center;justify-content:center;gap:14px;z-index:2}
.logo-mark{width:40px;height:40px;border-radius:50%;background:var(--green)}
.logo-name{font-family:"Cinzel",serif;font-weight:700;font-size:28px;color:var(--logo-blue);line-height:1}
.nav a{position:absolute;top:150px;font-family:"Cinzel",serif;font-size:23px;color:var(--white);white-space:nowrap;line-height:1;padding:10px 0;z-index:2}
.nav a.active{color:var(--green-light);border:2px solid var(--green-light);border-radius:12px;padding:9px 24px}
.arrow{position:absolute;top:362px;width:78px;height:78px;border:3px solid var(--green-light);border-radius:50%;z-index:2}
.arrow svg{position:absolute;left:25px;top:25px}
.hero-title{position:absolute;top:494px;width:1200px;text-align:center;font-family:"Cinzel",serif;font-size:78px;color:var(--white);line-height:1;text-transform:uppercase}
.hero-sub{position:absolute;top:568px;width:1200px;text-align:center;font-family:"Cinzel",serif;font-size:27px;color:var(--white);text-transform:uppercase;line-height:1}
.btn-light{position:absolute;left:528px;top:620px;width:140px;height:42px;background:var(--white);border-radius:4px;
  color:var(--green-dark);font-size:16px;display:flex;align-items:center;justify-content:center}

/* About */
.section-title{position:absolute;top:800px;width:1200px;text-align:center;font-family:"Cinzel",serif;font-size:60px;color:var(--green);line-height:1}
.rule{position:absolute;top:836px;height:2px;background:var(--green);width:276px}
.portrait{position:absolute;left:518px;top:876px;width:172px;height:172px;border-radius:50%;border:3px solid var(--green);
  background:radial-gradient(circle at 50% 40%,#c9d3db,#5d6f80)}
.about-text{position:absolute;left:210px;width:780px;text-align:center;font-size:13.5px;line-height:19px;color:#444}
.btn-outline{position:absolute;left:548px;top:1276px;width:120px;height:40px;border:1px solid var(--green);color:var(--green);
  font-size:16px;display:flex;align-items:center;justify-content:center}

/* Blog band */
.band{position:absolute;left:0;top:1374px;width:1200px;height:698px;background:var(--blue)}
.band-title{position:absolute;left:126px;top:1430px;font-family:"Cinzel",serif;font-size:34px;color:var(--white);line-height:1;text-transform:uppercase}
.band-sub{position:absolute;left:126px;top:1470px;font-size:21px;color:#dbe6f4}
.post{position:absolute;left:126px;width:606px;height:206px;border:1px solid var(--blue-line)}
.post-photo{position:absolute;left:22px;top:24px;width:146px;height:156px}
.post h3{position:absolute;left:184px;top:20px;font-size:23px;color:var(--white)}
.post p{position:absolute;left:184px;top:56px;width:400px;font-size:12.5px;line-height:17px;color:var(--white)}
.post .btn-small{position:absolute;left:184px;top:156px;width:92px;height:28px;background:var(--white);color:#333;font-size:13px;
  display:flex;align-items:center;justify-content:center}
.pager{position:absolute;left:544px;top:1994px;display:flex;gap:10px;font-size:13px;color:var(--white);align-items:center}
.pager .current{border:1px solid var(--white);padding:1px 5px}

/* Services ribbon */
.services{position:absolute;left:762px;top:1366px;width:314px;height:640px;background:linear-gradient(#7aa838,var(--green) 40%,#5f8c26);
  border-radius:8px 8px 0 0;box-shadow:0 6px 10px rgba(0,0,0,.35)}
.services-fold{position:absolute;left:1076px;top:1366px}
.services h2{position:absolute;left:38px;top:60px;font-family:"Cinzel",serif;font-size:34px;color:var(--white);line-height:1.2}
.services ul{position:absolute;left:22px;top:112px;width:268px;list-style:none}
.services li{position:relative;padding:8px 0 8px 18px;border-bottom:1px solid rgba(255,255,255,.3);font-size:12.5px;line-height:16px;color:var(--white)}
.services li:last-child{border-bottom:0}
.services li svg{position:absolute;left:0;top:11px}

/* Map */
.map{position:absolute;left:0;top:2072px;width:1200px;height:556px;background:linear-gradient(135deg,#efe9dc,var(--map) 60%,#e3ddc9)}

/* Footer */
.footer{position:absolute;left:0;top:2628px;width:1200px;height:68px;background:var(--footer)}
.footer-links{position:absolute;top:14px;width:1200px;text-align:center;font-size:13px;color:#999}
.footer-links a{color:#999}
.footer-links a.active{color:var(--white)}
.footer-links span{margin:0 6px;color:#777}
.copyright{position:absolute;top:36px;width:1200px;text-align:center;font-size:13px;color:#999}
.to-top{position:absolute;left:1150px;top:12px;width:36px;height:36px;background:#4a4a4a}
.to-top svg{position:absolute;left:10px;top:12px}
</style>
</head>
<body>

<header class="hero">
  <div class="hero-visual" role="img" aria-label="Blue textured illustration of a head profile opening to reveal golden gears"></div>
  <div class="logo-tab"><span class="logo-mark"></span><span class="logo-name">Brindle<br>Counseling</span></div>
  <nav class="nav">
    <a class="active" href="#" style="left:94px">Home</a>
    <a href="#" style="left:232px">About Me</a>
    <a href="#" style="left:394px">Rates and Services</a>
    <a href="#" style="left:668px">Common Questions</a>
    <a href="#" style="left:960px">Contact</a>
  </nav>
  <a class="arrow" style="left:44px" href="#" aria-label="Previous slide"><svg width="22" height="22" viewBox="0 0 22 22"><path d="M14 3 6 11l8 8" fill="none" stroke="#8cc63f" stroke-width="4"/></svg></a>
  <a class="arrow" style="left:1076px" href="#" aria-label="Next slide"><svg width="22" height="22" viewBox="0 0 22 22"><path d="M8 3l8 8-8 8" fill="none" stroke="#8cc63f" stroke-width="4"/></svg></a>
  <h1 class="hero-title">Lorem Ipsum</h1>
  <p class="hero-sub">Dolor sit amet, consectetur adipiscing</p>
  <a class="btn-light" href="#">Learn More</a>
</header>

<section class="about">
  <div class="rule" style="left:158px"></div>
  <div class="rule" style="left:766px"></div>
  <h2 class="section-title">About Me</h2>
  <div class="portrait" role="img" aria-label="Portrait photo of Martin Hale"></div>
  <p class="about-text" style="top:1056px">Lorem ipsum dolor sit amet, consectetur adipiscing elit. Nulla lobortis consequat mauris, eget eleifend nunc viverra viverra. Ut ac risus odio. Aliquam pretium purus sed nulla feugiat blandit. Cras vel libero ut lacus.</p>
  <p class="about-text" style="top:1122px">Magna non tincidunt accumsan, justo arcu cursus ipsum, non porttitor sapien quam vel magna. Maecenas elit nisl, molestie nec dapibus nec, aliquet a erat. Donec scelerisque lacus a libero suscipit auctor volutpat enim euismod. Mauris porta, lacus ut ullamcorper sodales, mauris tortor feugiat purus, nec aliquam neque purus ac metus. Nunc eleifend leo quis nisl endrerit ultrices. Suspendisse quis feugiat elit. Fusce vitae dolor ac est tincidunt feugiat. Phasellus volutpat dui in sapien malesuada tempus placerat justo ultricies. Duis mollis ornare risus, ut consectetur mi tincidunt sit amet. Maecenas quis nibh ac orci tempus scelerisque ac et massa.</p>
  <a class="btn-outline" href="#">Read More</a>
</section>

<section class="band"></section>
<h2 class="band-title">Lorem ipsum dolor sit amet,</h2>
<p class="band-sub">Consectetur adipiscing elit. Nulla lobortis consequat mauris,</p>

<article class="post" style="top:1526px">
  <div class="post-photo" role="img" aria-label="Photo of a sad young woman sitting alone" style="background:linear-gradient(#6d6a66,#3b3a3c)"></div>
  <h3>Lorem ipsum dolor sit amet,</h3>
  <p>Lorem ipsum dolor sit amet, consectetur adipiscing elit. Nulla lobortis consequat mauris, eget eleifend nunc viverra viverra. Ut ac risus odio. Aliquam pretium purus sed nulla feugiat blandit. Cras vel libero ut lacus eleifend tempor. Phasellus eleifend, magna non tincidunt accum justo arcu cursus ipsum, non porttitor sapien quam vel magna.</p>
  <a class="btn-small" href="#">Read More</a>
</article>
<article class="post" style="top:1750px">
  <div class="post-photo" role="img" aria-label="Photo of a smiling child" style="background:linear-gradient(#8aa7c4,#8a4b3c)"></div>
  <h3>Lorem ipsum dolor sit amet,</h3>
  <p>Lorem ipsum dolor sit amet, consectetur adipiscing elit. Nulla lobortis consequat mauris, eget eleifend nunc viverra viverra. Ut ac risus odio. Aliquam pretium purus sed nulla feugiat blandit. Cras vel libero ut lacus eleifend tempor. Phasellus eleifend, magna non tincidunt accumsan, justo arcu cursus ipsum, non porttitor</p>
  <a class="btn-small" href="#">Read More</a>
</article>
<div class="pager"><span>Prev</span><span class="current">1</span><span>2</span><span>3</span><span>4</span><span>5</span><span>6</span><span>Next</span></div>

<svg class="services-fold" width="14" height="16" viewBox="0 0 14 16"><path d="M0 0h4q10 0 10 10v6L0 8z" fill="#3f6415"/></svg>
<aside class="services">
  <h2>Services</h2>
  <ul>
    <li><svg width="12" height="10" viewBox="0 0 12 10"><path d="M1 5l3 3 7-7" fill="none" stroke="#fff" stroke-width="2"/></svg>Lorem ipsum dolor sit amet, consectetur adipiscing elit. Nulla lobortis consequat mauris, eget eleifend nunc viverra</li>
    <li><svg width="12" height="10" viewBox="0 0 12 10"><path d="M1 5l3 3 7-7" fill="none" stroke="#fff" stroke-width="2"/></svg>Viverra. Ut ac risus odio. Aliquam pretium purus sed nulla feugiat blandit. Cras vel libero ut lacus eleifend tempor.</li>
    <li><svg width="12" height="10" viewBox="0 0 12 10"><path d="M1 5l3 3 7-7" fill="none" stroke="#fff" stroke-width="2"/></svg>Phasellus eleifend, magna non Lorem ipsum dolor sit amet, consectetur adipiscing elit. Nulla lobortis</li>
    <li><svg width="12" height="10" viewBox="0 0 12 10"><path d="M1 5l3 3 7-7" fill="none" stroke="#fff" stroke-width="2"/></svg>Consequat mauris, eget eleifend nunc viverra viverra. Ut ac risus odio. Aliquam pretium purus sed nulla feugiat</li>
    <li><svg width="12" height="10" viewBox="0 0 12 10"><path d="M1 5l3 3 7-7" fill="none" stroke="#fff" stroke-width="2"/></svg>Blandit. Cras vel libero ut lacus eleifend tempor. Phasellus eleifend, magna non</li>
    <li><svg width="12" height="10" viewBox="0 0 12 10"><path d="M1 5l3 3 7-7" fill="none" stroke="#fff" stroke-width="2"/></svg>Lorem ipsum dolor sit amet, consectetur adipiscing elit. Nulla lobortis consequat mauris, eget eleifend nunc viverra</li>
    <li><svg width="12" height="10" viewBox="0 0 12 10"><path d="M1 5l3 3 7-7" fill="none" stroke="#fff" stroke-width="2"/></svg>Viverra. Ut ac risus odio. Aliquam pretium purus sed nulla feugiat blandit. Cras vel libero ut lacus eleifend tempor.</li>
    <li><svg width="12" height="10" viewBox="0 0 12 10"><path d="M1 5l3 3 7-7" fill="none" stroke="#fff" stroke-width="2"/></svg>Phasellus eleifend, magna non Lorem ipsum dolor sit amet, consectetur adipiscing elit. Nulla lobortis</li>
  </ul>
</aside>

<div class="map" role="img" aria-label="Street map marking the location of the practice"></div>

<footer class="footer">
  <div class="footer-links"><a class="active" href="#">Home</a><span>»</span><a href="#">About Me</a><span>»</span><a href="#">Rates and Services</a><span>»</span><a href="#">Common Questions</a><span>»</span><a href="#">Contact</a></div>
  <p class="copyright">© Copyright 2014 Brindle Counseling, PLLC. All Rights Reserved.</p>
  <a class="to-top" href="#" aria-label="Back to top"><svg width="16" height="10" viewBox="0 0 16 10"><path d="M1 9l7-7 7 7" fill="none" stroke="#ccc" stroke-width="2"/></svg></a>
</footer>

</body>
</html>
```